Innovative Educational Technology Startup needs Business Cards!

"Campus Horizon" is an all-in-one, social profile based, online portal for Companies and Students to connect and carry out their brand ambassadorship tasks and requirements. The service allows for companies to more efficiently deploy brand ambassadorship opportunities to the millions of students actively seeking on-campus work experience.

Both educational and corporate tied into one (please keep that in mind for design purposes)
Updates

Project Deadline Extended
Reason: Need time to provide feedback to the several great designs that have been created! Thanks for the patience of one more day!

Target Market(s)

Those who get the card will more than likely be business men and working adults, but many educational instructors, professors, students, marketers, and propoective collegiate students will be the main target for these cards.

Industry/Entity Type

Business

Requirements
Must have
• Our Icon-Sized Logo (CH) must be a focus in regards to imagery.
• Color scheme must be Tiffany Blue/Black/White..(base of the card either white or black).
• www.campushorizonhub.com located somewhere on it, but not the main point of the card. (Logo is for that)
Should not have
• Childish or Tech-Only appeal.
• Basic font.
• Rather there be as little asymmetry in the card shape as possible. (curved edges is fine)

```html
<!DOCTYPE html>
<html lang="en">
<head>
<meta charset="utf-8">
<title>Campus Horizon – Business Cards</title>
<link href="https://fonts.googleapis.com/css2?family=Oxygen:wght@400;700&display=swap" rel="stylesheet">
<style>
  :root {
    --tiffany: #1aa7de;
    --ink: #231f20;
    --text: #3d3d3d;
    --paper: #ffffff;
    --backdrop: #e4e4e4;
  }
  * { margin: 0; padding: 0; box-sizing: border-box; }
  html, body { width: 1200px; height: 900px; overflow: hidden; }
  body {
    background: var(--backdrop);
    font-family: "Oxygen", "Helvetica Neue", Arial, sans-serif;
    color: var(--text);
    position: relative;
  }
  .card {
    position: absolute;
    left: 250px;
    width: 700px;
    height: 400px;
    background: var(--paper);
    box-shadow: 0 4px 14px rgba(0,0,0,0.12);
  }
  .card--front { top: 34px; }
  .card--back  { top: 466px; }

  /* Front */
  .brand {
    position: absolute;
    display: flex;
    align-items: center;
    gap: 16px;
  }
  .card--front .brand { left: 50px; top: 92px; }
  .brand__mark {
    width: 58px; height: 58px;
    background: var(--tiffany);
  }
  .brand__name {
    font-size: 32px;
    font-weight: 400;
    color: var(--ink);
    letter-spacing: 0.5px;
  }
  .holder {
    position: absolute;
    right: 42px; top: 118px;
    text-align: right;
  }
  .holder__name {
    font-weight: 700;
    font-size: 18px;
    color: var(--tiffany);
    letter-spacing: 0.5px;
  }
  .holder__title { font-size: 15px; margin-top: 2px; }
  .divider {
    position: absolute;
    left: 40px; right: 42px; top: 176px;
    height: 1.5px;
    background: var(--tiffany);
  }
  .address {
    position: absolute;
    left: 50px; top: 200px;
    display: flex; gap: 14px;
    font-size: 16px; line-height: 1.6;
  }
  .address svg { margin-top: 22px; flex: none; }
  .contacts {
    position: absolute;
    right: 42px; top: 200px;
    list-style: none;
    font-size: 16px;
    line-height: 1.6;
    text-align: right;
  }
  .contacts li {
    display: flex;
    justify-content: flex-end;
    align-items: center;
    gap: 12px;
  }
  .contacts .icon {
    width: 16px;
    display: inline-flex;
    justify-content: center;
    align-items: center;
  }
  .band {
    position: absolute;
    bottom: 36px;
    height: 26px;
  }
  .band--blue { left: 0; width: 452px; background: var(--tiffany); }
  .band--black { left: 458px; right: 0; background: var(--ink); }

  /* Back */
  .card--back .brand {
    left: 0; right: 0; top: 130px;
    flex-direction: column;
    gap: 22px;
  }
  .card--back .brand__mark { width: 72px; height: 72px; }
  .card--back .brand__name { font-size: 36px; }
  .website {
    position: absolute;
    left: 0; right: 0; bottom: 44px;
    text-align: center;
    font-size: 15px;
    color: var(--tiffany);
    letter-spacing: 0.5px;
  }
</style>
</head>
<body>

<section class="card card--front" aria-label="Business card front">
  <div class="brand">
    <div class="brand__mark"></div>
    <div class="brand__name">Campus Horizon</div>
  </div>

  <div class="holder">
    <div class="holder__name">DANA WELLS</div>
    <div class="holder__title">President</div>
  </div>

  <div class="divider"></div>

  <div class="address">
    <svg width="12" height="17" viewBox="0 0 12 17" aria-hidden="true">
      <path d="M6 0C2.7 0 0 2.6 0 5.9 0 10.3 6 17 6 17s6-6.7 6-11.1C12 2.6 9.3 0 6 0z" fill="var(--tiffany)"/>
      <circle cx="6" cy="6" r="2.3" fill="#fff"/>
    </svg>
    <p>000 Harbor Lane<br>Suite 000 Lakeview,<br>CA&nbsp; 90000</p>
  </div>

  <ul class="contacts">
    <li>000 000 0000
      <span class="icon">
        <svg width="16" height="12" viewBox="0 0 16 12" aria-hidden="true">
          <path d="M1 4C1 1 15 1 15 4L12 5 11 3H5L4 5z" fill="var(--tiffany)"/>
          <rect x="3" y="6" width="10" height="6" rx="1" fill="var(--tiffany)"/>
        </svg>
      </span>
    </li>
    <li>000 000 0000
      <span class="icon">
        <svg width="10" height="15" viewBox="0 0 10 15" aria-hidden="true">
          <rect x="0.5" y="0.5" width="9" height="14" rx="1.5" fill="none" stroke="var(--tiffany)"/>
          <rect x="2" y="2.5" width="6" height="5" fill="var(--tiffany)"/>
          <circle cx="5" cy="11.5" r="1" fill="var(--tiffany)"/>
        </svg>
      </span>
    </li>
    <li>name@horizonmail.com.au
      <span class="icon">
        <svg width="16" height="11" viewBox="0 0 16 11" aria-hidden="true">
          <rect x="0.75" y="0.75" width="14.5" height="9.5" fill="none" stroke="var(--tiffany)" stroke-width="1.5"/>
          <path d="M1 1l7 5.5L15 1" fill="none" stroke="var(--tiffany)" stroke-width="1.5"/>
        </svg>
      </span>
    </li>
  </ul>

  <div class="band band--blue"></div>
  <div class="band band--black"></div>
</section>

<section class="card card--back" aria-label="Business card back">
  <div class="brand">
    <div class="brand__mark"></div>
    <div class="brand__name">Campus Horizon</div>
  </div>
  <p class="website">www.campushorizonhub.com</p>
</section>

</body>
</html>
```